IT Company needs stationary design

Business cards, MS Word, PowerPoint, A4 notepad design base on our company logo. This must be a set of templates in the same style which could be used both for printable documents as well as for documents shared digitally via email, website etc. This should be a modern design which is still professional, so make sure content is well readable both in MS Word and MS PowerPoint templates.

Target Market(s)

SME and Corporate

Industry/Entity Type

It Company

Font styles to use
Sans Serif

Colors
0455a3
0692cd
f37122
ffc214

Requirements
Must have
• 1) Business cards design: modern but still professional
• 2) MS Word: mostly for IT project documents (business analysis, reports, specifications, etc.) must be professional and easy readable.
• 3) MS PowerPoint: first slide, normal slide, last slide.
• 4) A4 notepad: header (must), footer (must), some light design on the background (optionally)
Nice to have
• Business cards design: would be nice to have 2-4 color variations of the same design from one side - cover (for example part of the cards are blue, part of the cards are orange) and other side with contact details is identical.

```html
<!DOCTYPE html>
<html lang="en">
<head>
<meta charset="utf-8">
<title>Nexaloop stationery set</title>
<link rel="stylesheet" href="https://fonts.googleapis.com/css2?family=Quicksand:wght@400&family=Oswald:wght@600&family=Open+Sans:wght@400;600&display=swap">
<style>
  :root {
    --canvas: #ffffff;
    --dark: #141414;
    --dark-soft: #2a2a2a;
    --light: #f4f4f4;
    --light-mid: #c4c4c4;
    --ink: #222222;
    --white: #ffffff;
    --blue: #0692cd;
    --orange: #f37122;
    --yellow: #ffc214;
    --ring-dark: rgba(255,255,255,0.07);
    --ring-light: rgba(0,0,0,0.16);
    --texture-dark: rgba(255,255,255,0.13);
    --texture-light: rgba(0,0,0,0.13);
  }
  * { box-sizing: border-box; margin: 0; padding: 0; }
  html, body { width: 1000px; height: 1200px; overflow: hidden; background: var(--canvas); }
  .sheet { position: relative; width: 1000px; height: 1200px; }
  .panel { position: absolute; overflow: hidden; }
  .panel--dark { background: linear-gradient(135deg, var(--dark-soft), var(--dark) 65%); }
  .panel--light { background: radial-gradient(circle at 35% 40%, var(--light), var(--light-mid) 95%); }
  .card-back { left: 18px; top: 24px; width: 484px; height: 290px; }
  .card-front { left: 502px; top: 24px; width: 484px; height: 290px; }
  .banner { left: 18px; top: 328px; width: 964px; height: 490px; }
  .notepad { left: 18px; top: 836px; width: 204px; height: 364px; }
  .slide { left: 238px; top: 836px; width: 748px; height: 348px; }

  .texture { position: absolute; border-radius: 50%; filter: blur(6px); }
  .texture--dark { background: radial-gradient(ellipse at center, var(--texture-dark), rgba(255,255,255,0) 70%); }
  .texture--light { background: radial-gradient(ellipse at center, var(--texture-light), rgba(0,0,0,0) 70%); }

  .backdrop-ring { position: absolute; border-radius: 50%; border-style: solid; }
  .panel--dark .backdrop-ring { border-color: var(--ring-dark); }
  .panel--light .backdrop-ring { border-color: var(--ring-light); }

  .brand { position: absolute; display: flex; align-items: center; font-family: "Quicksand", sans-serif; font-weight: 400; white-space: nowrap; }
  .brand__ring { border-radius: 50%; border-style: solid; flex: none; }
  .brand--on-dark { color: var(--white); }
  .brand--on-dark .brand__ring { border-color: var(--white); }
  .brand--on-light { color: var(--ink); }
  .brand--on-light .brand__ring { border-color: var(--ink); }

  .contact { position: absolute; left: 34px; top: 174px; color: var(--ink); font-family: "Open Sans", sans-serif; }
  .contact__title { display: flex; align-items: center; gap: 6px; margin-bottom: 10px; }
  .contact__name { font-family: "Oswald", sans-serif; font-weight: 600; font-size: 19px; letter-spacing: 0.2px; }
  .contact__role { font-size: 10px; font-weight: 600; border-left: 2px solid var(--orange); padding-left: 5px; line-height: 14px; }
  .contact__grid { display: grid; grid-template-columns: 96px auto; row-gap: 4px; font-size: 10.5px; margin-bottom: 10px; }
  .contact__item { display: flex; align-items: center; gap: 6px; }
  .icon { width: 8px; height: 8px; flex: none; }
  .icon--phone { background: var(--yellow); border-radius: 1px; }
  .icon--mobile { border: 1px solid var(--blue); border-radius: 1px; width: 6px; }
  .icon--web { background: var(--blue); border-radius: 50%; }
  .icon--mail { background: var(--orange); height: 6px; }
  .contact__company { font-size: 8px; font-weight: 600; line-height: 11px; }
  .contact__address { font-size: 8px; line-height: 11px; }
</style>
</head>
<body>
<main class="sheet">

  <section class="panel panel--dark card-back" aria-label="Business card, cover side">
    <div class="texture texture--dark" style="left:-60px;top:-60px;width:460px;height:380px" role="img" aria-label="Fine outlined triangle texture"></div>
    <span class="backdrop-ring" style="left:240px;top:10px;width:400px;height:400px;border-width:16px"></span>
    <div class="brand brand--on-dark" style="left:230px;top:194px;font-size:31px;gap:14px">
      <span class="brand__ring" style="width:46px;height:46px;border-width:3px"></span>nexaloop
    </div>
  </section>

  <section class="panel panel--light card-front" aria-label="Business card, contact side">
    <span class="backdrop-ring" style="left:-40px;top:-40px;width:330px;height:330px;border-width:14px"></span>
    <div class="texture texture--light" style="left:240px;top:-40px;width:300px;height:380px" role="img" aria-label="Fine outlined triangle texture"></div>
    <div class="brand brand--on-light" style="left:16px;top:48px;font-size:27px;gap:12px">
      <span class="brand__ring" style="width:58px;height:58px;border-width:3px"></span>nexaloop
    </div>
    <div class="contact">
      <div class="contact__title">
        <span class="contact__name">FULL NAME</span>
        <span class="contact__role">General Director</span>
      </div>
      <div class="contact__grid">
        <span class="contact__item"><i class="icon icon--phone"></i>755 21 40 63</span>
        <span class="contact__item"><i class="icon icon--web"></i>www.nexaloop.com</span>
        <span class="contact__item"><i class="icon icon--mobile"></i>759 62 18 27</span>
        <span class="contact__item"><i class="icon icon--mail"></i>info@nexaloop.com</span>
      </div>
      <p class="contact__company">Nexaloop Communication Incorporated</p>
      <p class="contact__address">West 18th Avenue, 2nd Floor, Portland, OR 205, USA</p>
    </div>
  </section>

  <section class="panel panel--dark banner" aria-label="Presentation title slide">
    <div class="texture texture--dark" style="left:-40px;top:-60px;width:660px;height:560px" role="img" aria-label="Fine outlined triangle texture"></div>
    <span class="backdrop-ring" style="left:540px;top:10px;width:500px;height:500px;border-width:22px"></span>
    <div class="brand brand--on-dark" style="left:58px;top:344px;font-size:44px;gap:22px">
      <span class="brand__ring" style="width:100px;height:100px;border-width:5px"></span>nexaloop
    </div>
  </section>

  <section class="panel panel--light notepad" aria-label="Notepad page">
    <span class="backdrop-ring" style="left:0;top:20px;width:340px;height:340px;border-width:14px"></span>
    <div class="texture texture--light" style="left:40px;top:-20px;width:200px;height:400px" role="img" aria-label="Fine outlined triangle texture"></div>
    <div class="brand brand--on-light" style="left:30px;top:128px;font-size:17px;gap:8px">
      <span class="brand__ring" style="width:42px;height:42px;border-width:2px"></span>nexaloop
    </div>
  </section>

  <section class="panel panel--light slide" aria-label="Presentation closing slide">
    <span class="backdrop-ring" style="left:20px;top:-90px;width:580px;height:580px;border-width:18px"></span>
    <div class="texture texture--light" style="left:480px;top:-40px;width:320px;height:430px" role="img" aria-label="Fine outlined triangle texture"></div>
    <div class="brand brand--on-light" style="left:82px;top:98px;font-size:62px;gap:36px">
      <span class="brand__ring" style="width:168px;height:168px;border-width:7px"></span>nexaloop
    </div>
  </section>

</main>
</body>
</html>
```